RWT Installations Ltd Business Cards

We need a business card with our business logo. We provide window and door installations on high-rises in west coast British Colombia, Canada.

I would like my business information and details on one side of the card, and the other side the company name with logo

Target Market(s)

General Contractors

Industry/Entity Type

Construction

Contact Information for Business Card

one side i want my company name and logo in the dark theme logo that i provided

Requirements
Must have
• Tomas Verelund, 15559284016, RWTInstallations@mailvera.example, 1408-5192 Pellow Avenue Burnaby BC, V0X 1Z9, Owner & Manager

```html
<!DOCTYPE html>
<html lang="en">
<head>
<meta charset="utf-8">
<title>RWT Installations Ltd — Business Cards</title>
<link rel="stylesheet" href="https://fonts.googleapis.com/css2?family=Raleway:wght@400;500;700&display=swap">
<style>
  :root {
    --backdrop: #b3b3b3;
    --card: #ffffff;
    --brand-blue: #27a9e1;
    --brand-grey: #9b9b9b;
    --ink-light: #ffffff;
  }
  html, body {
    margin: 0;
    width: 1200px;
    height: 1200px;
    overflow: hidden;
    background: var(--backdrop);
  }
  .canvas {
    position: relative;
    width: 1200px;
    height: 1200px;
    font-family: "Raleway", sans-serif;
  }
  .card {
    position: absolute;
    left: 166px;
    width: 867px;
    background: var(--card);
    box-shadow: 0 2px 6px rgba(0, 0, 0, 0.28);
  }
  .card svg { display: block; width: 100%; height: 100%; }
  .card--front { top: 72px; height: 507px; }
  .card--back { top: 622px; height: 509px; }
  .fill-blue { fill: var(--brand-blue); }
  .fill-grey { fill: var(--brand-grey); }
  .wordmark {
    font-family: "Raleway", sans-serif;
    font-weight: 700;
    fill: var(--brand-blue);
    letter-spacing: 0.5px;
  }
  .holder-name {
    font-family: "Raleway", sans-serif;
    font-weight: 700;
    font-size: 24px;
    fill: var(--ink-light);
  }
  .holder-role {
    font-family: "Raleway", sans-serif;
    font-weight: 500;
    font-size: 15px;
    fill: var(--ink-light);
  }
  .contact-line {
    font-family: "Raleway", sans-serif;
    font-weight: 400;
    font-size: 13px;
    fill: var(--ink-light);
  }
  .contact-icon { fill: var(--ink-light); }
</style>
</head>
<body>
<main class="canvas">

  <!-- Contact side -->
  <section class="card card--front" aria-label="Business card, contact side">
    <svg viewBox="0 0 693 405" preserveAspectRatio="none">
      <g class="brand-lockup">
        <rect class="fill-grey" x="186" y="88" width="24" height="24"/>
        <text class="wordmark" x="220" y="108" font-size="20.5">RWT INSTALLATIONS LTD</text>
      </g>

      <polygon class="fill-blue name-band" points="0,234 427,234 329,370 0,370"/>
      <polygon class="fill-grey contact-band" points="437,234 693,234 693,405 0,405 0,379 335,379"/>

      <text class="holder-name" x="300" y="298" text-anchor="end">TOMAS VERELUND</text>
      <text class="holder-role" x="300" y="324" text-anchor="end">Owner &amp; Manager</text>

      <text class="contact-line" x="648" y="286" text-anchor="end">15559284016</text>
      <text class="contact-line" x="648" y="310" text-anchor="end">RWTInstallations@mailvera.example</text>
      <text class="contact-line" x="648" y="334" text-anchor="end">1408-5192 Pellow Avenue</text>
      <text class="contact-line" x="648" y="350" text-anchor="end">Burnaby BC, V0X 1Z9</text>

      <g class="contact-icon">
        <path d="M660.5 276.5 c0.8-0.8 1.8-0.8 2.3 0 l1.2 1.8 c0.4 0.6 0.2 1.3-0.3 1.7 l-0.7 0.5 c0.7 1.6 1.8 2.7 3.4 3.4 l0.5-0.7 c0.4-0.5 1.1-0.7 1.7-0.3 l1.8 1.2 c0.8 0.5 0.8 1.5 0 2.3 l-0.8 0.8 c-4.5 0.6-10.1-5-9.5-9.5z"/>
        <rect x="660" y="301" width="11" height="8" rx="1"/>
        <polyline points="660.5,301.8 665.5,305.8 670.5,301.8" fill="none" stroke="#9b9b9b" stroke-width="1"/>
        <path d="M665.5 325 a4.5 4.5 0 0 1 4.5 4.5 c0 3.2-4.5 7.5-4.5 7.5 s-4.5-4.3-4.5-7.5 a4.5 4.5 0 0 1 4.5-4.5z"/>
        <circle cx="665.5" cy="329.5" r="1.6" fill="#9b9b9b"/>
      </g>
    </svg>
  </section>

  <!-- Brand side -->
  <section class="card card--back" aria-label="Business card, brand side">
    <svg viewBox="0 0 693 407" preserveAspectRatio="none">
      <polygon class="fill-grey corner-panel" points="434,0 693,0 693,390"/>
      <polygon class="fill-blue base-band" points="0,302 580,302 529,215 567,215 688,407 0,407"/>

      <g class="brand-lockup">
        <rect class="fill-grey" x="81" y="160" width="34" height="34"/>
        <text class="wordmark" x="127" y="187" font-size="25">RWT INSTALLATIONS LTD</text>
      </g>
    </svg>
  </section>

</main>
</body>
</html>
```